Comp & Pen Prep Tip Sheet for Veterans

I need a flyer/brochure/card with tips to help prepare veterans for their upcoming Comp & Pen Exams. Needs to be colorful and have vectors/images that correspond with teach tip. I have attached a word document with the language to include. This will go out with our welcome kit for veterans to reference before their exam.

Target Market(s)

Veterans

Industry/Entity Type

Legal/Non-Profit Organization/Medical

Colors
0054AA
0677BA
7BADD7
CADEEF
E8F1F8

Requirements
Must have
• Vectors/easy to follow

```html
<!DOCTYPE html>
<html lang="en">
<head>
<meta charset="utf-8">
<title>The Comp &amp; Pen Exam – Tip Sheet</title>
<link href="https://fonts.googleapis.com/css2?family=Oswald:wght@500;700&family=Open+Sans:wght@400;600;700&display=swap" rel="stylesheet">
<style>
:root{
  --navy:#0b1a4a;
  --blue-deep:#1a3f8f;
  --blue:#1f56b0;
  --blue-mid:#0677ba;
  --blue-light:#7badd7;
  --red:#e3202e;
  --ink:#2b2b2b;
  --heading:#1d3b7a;
  --cell:#f3f3f3;
  --white:#ffffff;
}
*{margin:0;padding:0;box-sizing:border-box}
html,body{width:1200px;height:1200px;overflow:hidden;background:var(--white)}
.flyer{position:relative;width:1200px;height:1200px;font-family:"Open Sans",sans-serif;color:var(--ink);background:var(--white)}
.hero-photo{position:absolute;left:0;top:0;width:1200px;height:300px;
  background:radial-gradient(ellipse at 72% 45%,#8d8a6a 0%,#6f6f52 35%,#4f5a45 70%,#3e4838 100%)}
.hero-band{position:absolute;left:0;top:0;width:1200px;height:580px}
.brand{position:absolute;left:40px;top:60px;width:240px;text-align:center}
.brand-name{display:flex;align-items:center;justify-content:center;gap:8px;font-weight:700;font-size:20px;color:var(--white);line-height:1.15}
.brand-name .dot{flex:none;width:14px;height:14px;border-radius:50%;background:var(--white)}
.brand-tag{margin-top:8px;font-size:11px;font-weight:600;color:#1f1f1f;background:rgba(255,255,255,.75);display:inline-block;padding:2px 8px}
.intro{position:absolute;left:0;top:250px;width:1200px;text-align:center;color:var(--white)}
.title{font-family:"Oswald",sans-serif;font-weight:700;font-size:64px;letter-spacing:1px;line-height:1;text-shadow:3px 3px 0 #0d2a6e}
.intro p{font-size:15.5px;line-height:1.42;margin:12px auto 0;width:1100px}
.ribbon{position:absolute;left:50%;transform:translateX(-50%);color:var(--white);font-weight:700;text-align:center;white-space:nowrap}
.ribbon svg{position:absolute;inset:0;width:100%;height:100%;z-index:0}
.ribbon span{position:relative;z-index:1}
.ribbon-top{top:505px;width:960px;height:30px;font-size:16px;line-height:30px}
.remember{position:absolute;left:0;top:538px;width:1200px;height:50px;background:var(--blue-deep);
  font-family:"Oswald",sans-serif;font-weight:700;font-size:40px;line-height:50px;color:var(--white);text-align:center;letter-spacing:.5px}
.tips{position:absolute;left:0;top:588px;width:1200px;height:528px;display:grid;grid-template-columns:repeat(3,1fr);grid-template-rows:repeat(2,1fr);gap:2px;background:#ffffff}
.tip{background:linear-gradient(180deg,#f7f7f7,#ececec);padding:10px 30px 0;text-align:center}
.tip svg{width:40px;height:40px;display:block;margin:0 auto}
.tip h2{font-family:"Oswald",sans-serif;font-weight:500;font-size:25px;color:var(--heading);margin:4px 0 6px;line-height:1.1}
.tip p{font-size:13.4px;line-height:1.4;text-align:justify;text-align-last:center}
.tip p + p{margin-top:10px}
.ribbon-bottom{top:1124px;width:680px;height:28px;font-size:16px;line-height:28px}
.footer-stripes{position:absolute;left:0;bottom:0;width:1200px;height:26px}
</style>
</head>
<body>
<main class="flyer">
  <div class="hero-photo" role="img" aria-label="Close-up photo of a camouflage uniform shoulder with an embroidered flag patch"></div>
  <svg class="hero-band" viewBox="0 0 1200 580" preserveAspectRatio="none" aria-hidden="true">
    <defs>
      <linearGradient id="bandFill" x1="0" y1="0" x2="0" y2="1">
        <stop offset="0" stop-color="#1a4aa8"/>
        <stop offset="0.55" stop-color="#2a62c0"/>
        <stop offset="1" stop-color="#1a47a0"/>
      </linearGradient>
    </defs>
    <path d="M0 200 Q560 400 1200 200 L1200 580 L0 580 Z" fill="url(#bandFill)"/>
    <path d="M0 200 Q560 400 1200 200 L1200 212 Q560 412 0 212 Z" fill="#0d2f7a"/>
  </svg>

  <div class="brand">
    <div class="brand-name"><span class="dot"></span>Harbor Veterans Alliance</div>
    <div class="brand-tag">Serving Veterans Since 1993</div>
  </div>

  <section class="intro">
    <h1 class="title">THE COMP &amp; PEN EXAM</h1>
    <p>The Comp &amp; Pen Exam is your opportunity to present all the reasons you believe your condition is related to service to the physician.</p>
    <p>If your condition is not already service-connected, be sure to talk to the examiner about what happened in service that could have led to your current condition. The examiner will review your file, including your statements, service records, and treatment records, and provide a medical opinion as to whether your condition was caused or aggravated by your military service.</p>
    <p>The examiner will be observing your movements and behavior and may perform a limited physical exam to evaluate your condition.</p>
  </section>

  <div class="ribbon ribbon-top">
    <svg viewBox="0 0 960 30" preserveAspectRatio="none" aria-hidden="true"><polygon points="0,0 960,0 945,30 15,30" fill="#e3202e"/></svg>
    <span>After your Comp &amp; Pen Exam, make sure you complete the Comp &amp; Pen Exit Survey based on your experience</span>
  </div>

  <h2 class="remember">THINGS TO REMEMBER FOR YOUR EXAM</h2>

  <section class="tips">
    <article class="tip">
      <svg viewBox="0 0 40 40" aria-hidden="true"><circle cx="15" cy="17" r="7" fill="#e3202e"/><path d="M3 38 Q3 26 15 26 Q27 26 27 38 Z" fill="#e3202e"/><path d="M24 3 h13 a2 2 0 0 1 2 2 v7 a2 2 0 0 1-2 2 h-9 l-4 3 v-3 a2 2 0 0 1-2-2 v-7 a2 2 0 0 1 2-2z" fill="none" stroke="#e3202e" stroke-width="1.6"/><circle cx="27" cy="8.5" r="1" fill="#e3202e"/><circle cx="30.5" cy="8.5" r="1" fill="#e3202e"/><circle cx="34" cy="8.5" r="1" fill="#e3202e"/></svg>
      <h2>1.&nbsp; Talk About Your Service</h2>
      <p>Talk about what happened in service that you believe caused or aggravated your condition. Try to be as specific as possible. If you are not comfortable discussing the details of an in-service event, you may point to statements you submitted to the VA previously for the examiner to reference. If you can, provide the examiner with a copy of these statements on the day of the exam.</p>
    </article>
    <article class="tip">
      <svg viewBox="0 0 40 40" aria-hidden="true"><circle cx="20" cy="20" r="16" fill="none" stroke="#e3202e" stroke-width="2.4"/><circle cx="20" cy="8" r="3.2" fill="#e3202e"/><rect x="16" y="12" width="8" height="13" rx="2" fill="#e3202e"/><rect x="16.5" y="24" width="3" height="10" fill="#e3202e"/><rect x="20.5" y="24" width="3" height="10" fill="#e3202e"/><rect x="7" y="14" width="26" height="3" rx="1.5" fill="#e3202e"/></svg>
      <h2>2.&nbsp; Trace Your Symptoms</h2>
      <p>Discuss what symptoms you experienced immediately following your injury in service and how these symptoms have worsened over time.</p>
      <p>Your statement will help trace the start of your symptoms back to what happened during service.</p>
    </article>
    <article class="tip">
      <svg viewBox="0 0 40 40" aria-hidden="true"><path d="M20 36 L5 21 A8.5 8.5 0 0 1 20 9 A8.5 8.5 0 0 1 35 21 Z" fill="#e3202e"/><path d="M13 25 L21 17 M16 28 L24 20 M19 31 L26 24" stroke="#fff" stroke-width="2.2" stroke-linecap="round"/></svg>
      <h2>3.&nbsp; Be Honest</h2>
      <p>Be honest when describing the frequency and severity of your symptoms and how they impact your day-to-day life to the examiner; do not downplay the severity of your symptoms.</p>
      <p>Keep in mind that the examiner will be closely monitoring your movements and behavior, including your body language and the tone of your voice.</p>
    </article>
    <article class="tip">
      <svg viewBox="0 0 40 40" aria-hidden="true"><circle cx="20" cy="27" r="11" fill="none" stroke="#e3202e" stroke-width="2.6"/><circle cx="20" cy="27" r="5" fill="#e3202e"/><path d="M20 2 v8 M9 5 l4 7 M31 5 l-4 7 M4 12 l6 4 M36 12 l-6 4" stroke="#e3202e" stroke-width="2.2" stroke-linecap="round"/></svg>
      <h2>4.&nbsp; Pain</h2>
      <p>While the exam is not meant to be painful, you may experience slight discomfort depending on the required testing.</p>
      <p>When testing your range of motion, be sure to tell the examiner AS SOON AS you begin to experience pain, as this contributes to your overall functional loss and should be considered in your rating.</p>
    </article>
    <article class="tip">
      <svg viewBox="0 0 40 40" aria-hidden="true"><circle cx="11" cy="24" r="5" fill="#e3202e"/><path d="M2 39 Q2 31 11 31 Q20 31 20 39 Z" fill="#e3202e"/><path d="M18 3 h19 a2 2 0 0 1 2 2 v12 a2 2 0 0 1-2 2 h-12 l-5 4 v-4 h-2 a2 2 0 0 1-2-2 v-12 a2 2 0 0 1 2-2z" fill="none" stroke="#e3202e" stroke-width="1.8"/><path d="M20 9 h7 M20 13 h6" stroke="#e3202e" stroke-width="1.6"/><text x="32" y="16" font-family="Open Sans,sans-serif" font-weight="700" font-size="11" fill="#e3202e" text-anchor="middle">?</text></svg>
      <h2>5.&nbsp; Ask for Clarification</h2>
      <p>Do not answer a question you do not understand. Ask for clarification if necessary. Do not talk to fill the space or time. Keep your conversation with the examiner limited to what happened in service, the frequency and severity of symptoms related to your condition, and how they impact your day-to-day life.</p>
    </article>
    <article class="tip">
      <svg viewBox="0 0 40 40" aria-hidden="true"><rect x="8" y="3" width="16" height="6" rx="1" fill="#e3202e"/><rect x="6" y="10" width="20" height="27" rx="3" fill="#e3202e"/><path d="M16 17 v13 M9.5 23.5 h13" stroke="#fff" stroke-width="3"/><rect x="28" y="25" width="10" height="6" rx="3" fill="#e3202e"/><circle cx="32" cy="35" r="3.5" fill="#e3202e"/></svg>
      <h2>6.&nbsp; Medications</h2>
      <p>If you are prescribed any medication(s) for your condition, be sure to tell the examiner the name and dosage of each medication and how often you take each. This is extremely important, because medication may mask some of your symptoms, or the use of medication(s) may be used to evaluate the severity of your condition and how much it impacts your ability to work.</p>
    </article>
  </section>

  <div class="ribbon ribbon-bottom">
    <svg viewBox="0 0 680 28" preserveAspectRatio="none" aria-hidden="true"><polygon points="0,0 680,0 664,28 16,28" fill="#e3202e"/></svg>
    <span>Please complete the Comp &amp; Pen Exit Survey after your Comp &amp; Pen Exam</span>
  </div>

  <svg class="footer-stripes" viewBox="0 0 1200 26" preserveAspectRatio="none" aria-hidden="true">
    <polygon points="0,0 800,0 780,26 0,26" fill="#1f56b0"/>
    <polygon points="800,0 812,0 792,26 780,26" fill="#ffffff"/>
    <polygon points="812,0 1200,0 1200,26 792,26" fill="#e3202e"/>
  </svg>
</main>
</body>
</html>
```